Electrical Engineering Business Card Design

I need a business card design for an engineering consulting company based in Orlando, FL. I have had a logo created which the files are attached. We work primarily in the theme park and entertainment market sector but do projects in all market sectors. We have been serving Central Florida since 1994 and continue to strive to serve our clients and provide outstanding designs.
Industry/Entity Type
Theme Park

```html
<!DOCTYPE html>
<html lang="en">
<head>
<meta charset="utf-8">
<title>Velmar Associates – Business Card</title>
<link rel="stylesheet" href="https://fonts.googleapis.com/css2?family=Oswald:wght@400&family=Open+Sans:wght@400;600&display=swap">
<style>
  :root {
    --brand-green: #84c242;
    --card-white: #ffffff;
    --ink: #111111;
    --backdrop: #e9e4dc;
  }
  html, body {
    margin: 0;
    padding: 0;
    overflow: hidden;
  }
  .canvas {
    position: relative;
    width: 1200px;
    height: 438px;
    background: var(--backdrop);
    overflow: hidden;
  }
  .card-shape {
    position: absolute;
    left: 0;
    top: 0;
  }
  .card-front__name {
    position: absolute;
    left: 142px;
    top: 166px;
    width: 360px;
    text-align: center;
    font-family: "Oswald", sans-serif;
    font-weight: 400;
    font-size: 96px;
    line-height: 1;
    color: var(--card-white);
    letter-spacing: 2px;
  }
  .company-name {
    position: absolute;
    left: 727px;
    top: 150px;
    margin: 0;
    font-family: "Oswald", sans-serif;
    font-weight: 400;
    font-size: 25px;
    line-height: 1;
    color: var(--ink);
  }
  .company-city {
    position: absolute;
    left: 757px;
    top: 188px;
    margin: 0;
    font-family: "Open Sans", sans-serif;
    font-weight: 600;
    font-size: 10px;
    letter-spacing: 2.6px;
    color: var(--ink);
  }
  .mailing-address {
    position: absolute;
    left: 728px;
    top: 226px;
    margin: 0;
    font-family: "Open Sans", sans-serif;
    font-weight: 600;
    font-style: normal;
    font-size: 15px;
    line-height: 20px;
    color: var(--ink);
  }
  .contact-band {
    position: absolute;
    left: 728px;
    top: 279px;
    font-family: "Open Sans", sans-serif;
    font-size: 15px;
    line-height: 20px;
    color: var(--card-white);
  }
  .contact-band__phone {
    position: absolute;
    left: 192px;
    top: 0;
    white-space: nowrap;
  }
  .contact-fax {
    position: absolute;
    left: 920px;
    top: 305px;
    font-family: "Open Sans", sans-serif;
    font-weight: 600;
    font-size: 11px;
    color: var(--brand-green);
  }
</style>
</head>
<body>
<main class="canvas">
  <svg class="card-shape" width="1200" height="438" viewBox="0 0 1200 438" aria-hidden="true">
    <polygon class="card-front" points="142,120 464,120 553,254 553,335 142,335" fill="var(--brand-green)"/>
    <polygon class="card-back" points="725,122 1040,122 1040,331 643,331 643,254" fill="var(--card-white)" stroke="var(--brand-green)" stroke-width="3"/>
    <rect class="card-back__band" x="643" y="278" width="397" height="22" fill="var(--brand-green)"/>
  </svg>

  <div class="card-front__name">VMA</div>

  <h1 class="company-name">Velmar Associates, P.A.</h1>
  <p class="company-city">ORLANDO, FLORIDA</p>

  <address class="mailing-address">PO Box 550217<br>Orlando, FL 32899</address>

  <div class="contact-band">
    <span class="contact-band__email">velmar.lee@mailbox.com</span>
    <span class="contact-band__phone">407-555-0148</span>
  </div>
  <div class="contact-fax">fax: 407-555-0192</div>
</main>
</body>
</html>
```